Premium label design for product needed

UPDATE: (Scroll down)
For a face care product i need a new front label on the bottle. The current one is white and i want to add the franchise color green. The objective is to premiunize the packaging and to give guidance to the consumers to find their franchise color. The task is to find several option to color the label on the bottle in the most premium way. But at the same time it should not be playful, more in a serious medical direction or in a counterbrand direction. It should look absolutely premium. but should not shout to much. The text structure should remain the same. I will provide a powerpoint slide to illustrate the task even clearer.
UPDATE: DO NOT DESIGN THE FOLDING BOX, only design the bottle. The folding box only serves the purpose of giving the text/layout structure and rough color intent.

Target Market(s)

female 25-39

Requirements
Must have
• Premium, Uniqueness, Innovative

```html
<!DOCTYPE html>
<html lang="en">
<head>
<meta charset="UTF-8">
<title>Bottle Label Options</title>
<link rel="stylesheet" href="https://fonts.googleapis.com/css2?family=Montserrat:wght@500;600;700&display=swap">
<style>
  :root {
    --page-bg: #ffffff;
    --bottle-body: #f6f6f7;
    --bottle-edge: #dcdcdf;
    --seam: #e2e2e5;
    --tag-bg: #000000;
    --tag-text: #ffffff;
    --green-light: #b0dbb5;
    --green-deep: #7daf80;
    --ink: #1c1c1c;
    --white: #ffffff;
    --accent-red: #a0122a;
  }
  * { margin: 0; padding: 0; box-sizing: border-box; }
  html, body {
    width: 888px;
    height: 1200px;
    overflow: hidden;
    background: var(--page-bg);
  }
  body {
    position: relative;
    font-family: "Montserrat", Arial, sans-serif;
  }
  .option {
    position: absolute;
    top: 0;
    width: 250px;
    height: 1200px;
  }
  .option--one { left: 124px; }
  .option--two { left: 514px; }

  .option-tag {
    position: absolute;
    top: 107px;
    left: 90px;
    width: 70px;
    height: 47px;
    background: var(--tag-bg);
    color: var(--tag-text);
    border-radius: 5px;
    font-weight: 700;
    font-size: 24px;
    line-height: 47px;
    text-align: center;
    letter-spacing: 0.02em;
  }

  .bottle {
    position: absolute;
    top: 228px;
    left: 0;
    width: 250px;
    height: 796px;
    background: var(--bottle-body);
    border: 1px solid var(--bottle-edge);
    border-radius: 6px;
    overflow: hidden;
  }
  .bottle-seam {
    position: absolute;
    left: 0;
    width: 100%;
    height: 1px;
    background: var(--seam);
  }
  .bottle-seam--cap { top: 229px; }
  .bottle-seam--collar { top: 277px; }

  .label-band {
    position: absolute;
    top: 454px;
    left: 0;
    width: 100%;
    height: 158px;
    display: flex;
    flex-direction: column;
    justify-content: center;
    align-items: center;
  }
  .option--one .label-band { background: var(--green-light); color: var(--ink); }
  .option--two .label-band { background: var(--green-deep); color: var(--white); }

  .product-name {
    font-weight: 700;
    font-size: 27px;
    line-height: 35px;
    letter-spacing: 0.12em;
    text-align: left;
    width: 196px;
    margin-left: 6px;
  }
  .product-name span { display: block; }

  .product-type {
    position: absolute;
    top: 678px;
    left: 0;
    width: 100%;
    text-align: center;
    font-weight: 500;
    font-size: 13.5px;
    letter-spacing: 0.14em;
    color: var(--ink);
  }
  .product-line {
    position: absolute;
    top: 738px;
    left: 0;
    width: 100%;
    text-align: center;
    font-weight: 700;
    font-size: 11px;
    letter-spacing: 0.13em;
    color: var(--accent-red);
  }
</style>
</head>
<body>

  <section class="option option--one">
    <div class="option-tag">01</div>
    <div class="bottle">
      <div class="bottle-seam bottle-seam--cap"></div>
      <div class="bottle-seam bottle-seam--collar"></div>
      <div class="label-band">
        <h1 class="product-name"><span>PURE SKIN</span><span>FORMULA</span></h1>
      </div>
      <p class="product-type">A.I. MATT FLUID</p>
      <p class="product-line">DERMATOLOGICAL SKINCARE</p>
    </div>
  </section>

  <section class="option option--two">
    <div class="option-tag">02</div>
    <div class="bottle">
      <div class="bottle-seam bottle-seam--cap"></div>
      <div class="bottle-seam bottle-seam--collar"></div>
      <div class="label-band">
        <h1 class="product-name"><span>PURE SKIN</span><span>FORMULA</span></h1>
      </div>
      <p class="product-type">A.I. MATT FLUID</p>
      <p class="product-line">DERMATOLOGICAL SKINCARE</p>
    </div>
  </section>

</body>
</html>
```